Tea box package for Herbal Teas

We would like a design for a package of our tea products. We want the consumer to understand that our products are natural just by looking at the package. We prefer minimalistic designs.
The package we want would be a square (or slightly rectangular) box. The box would be generic enough for us to use it for different teas. Essentially what we want is all the main information and designs to be the same for each tea product we have. We would like to be able to change the main color and the name of the tea then to customize to the tea in the package. Please see the attached images for examples.
We really like the package in tea_packaging_example_4 picture. We would like our packaging to be something very similar but with all the labels printed on the package.
We already have our logo so I am attaching that as well (image named 'velka brin logo copy'). That would go on the front of the box.
We also attach a tile created using our logo (see image called 'tile'). We would like this to go to the sides similarly to tea_packaging_example_4.
On the back of the pouch, we want to have directions on how to make the tea but we want this section to be editable. For now just 3-4 lines of sample text is fine along with instructions on how to make a tea, see picture 'back of tea box'.
We would like for the box color to be as in example picture
tea_packaging_example_4. The color of the writing should be the same as the logo color. The font style should be something that would look nice next to the logo font, we are not sure what that font should be. The only thing colored would be the name of the tea and the ribbon as seen in tea_packaging_example_4, which we would like to change if we need to, to other variations.
Thanks a lot. For any questions, please contact me.

```html
<!DOCTYPE html>
<html lang="en">
<head>
<meta charset="utf-8">
<title>Velka Brin Green Tea – Box Dieline</title>
<link rel="stylesheet" href="https://fonts.googleapis.com/css2?family=Libre+Baskerville:wght@400;700&family=Montserrat:wght@400&family=Kalam:wght@400;700&display=swap">
<style>
  :root {
    --paper: #ffffff;
    --wood: #dcb98b;
    --wood-light: #e6c89d;
    --wood-dark: #cfa874;
    --ink: #231f20;
    --ribbon: #fbc762;
    --label-white: #ffffff;
    --note: #f7f6f2;
    --pattern-a: #c99a5c;
    --pattern-b: #a97c44;
  }
  html, body { margin: 0; padding: 0; overflow: hidden; background: var(--paper); }
  .canvas { width: 1200px; height: 906px; position: relative; }
  .dieline { display: block; }
  .wood { fill: url(#woodGrain); }
  .panel-edge { fill: none; stroke: var(--ink); stroke-width: 3; }
  .caption { font-family: "Montserrat", sans-serif; font-size: 14px; fill: var(--ink); }
  .brand { font-family: "Libre Baskerville", serif; fill: var(--ink); }
  .tagline { font-family: "Libre Baskerville", serif; font-size: 10px; fill: var(--ink); }
  .tea-name { font-family: "Libre Baskerville", serif; font-weight: 700; fill: var(--ink); }
  .footer-line { font-family: "Libre Baskerville", serif; font-size: 5.5px; fill: #e8e8e8; }
  .note-head { font-family: "Kalam", cursive; font-weight: 700; font-size: 9px; fill: var(--ink); }
  .note-body { font-family: "Kalam", cursive; font-size: 5.6px; fill: var(--ink); }
  .frame-line { fill: none; stroke: #bdbdbd; stroke-width: 1; }
</style>
</head>
<body>
<div class="canvas">
<svg class="dieline" width="1200" height="906" viewBox="0 0 1200 906" xmlns="http://www.w3.org/2000/svg">
  <defs>
    <linearGradient id="woodGrain" x1="0" y1="0" x2="1" y2="0.15">
      <stop offset="0" stop-color="var(--wood-dark)"/>
      <stop offset="0.3" stop-color="var(--wood-light)"/>
      <stop offset="0.6" stop-color="var(--wood)"/>
      <stop offset="1" stop-color="var(--wood-light)"/>
    </linearGradient>
    <radialGradient id="tileTone" cx="0.5" cy="0.5" r="0.7">
      <stop offset="0" stop-color="var(--pattern-a)"/>
      <stop offset="1" stop-color="var(--pattern-b)"/>
    </radialGradient>
  </defs>

  <!-- Sticker -->
  <g class="sticker">
    <rect x="130" y="82" width="129" height="45" fill="var(--ribbon)"/>
    <text class="tagline" x="194.5" y="100" text-anchor="middle">100% ORGANIC PURE</text>
    <text class="tea-name" x="194.5" y="117" font-size="16" text-anchor="middle">GREEN TEA</text>
    <text class="caption" x="194.5" y="149" text-anchor="middle">Sticker</text>
  </g>

  <!-- Captions -->
  <text class="caption" x="469" y="363" text-anchor="middle">Front</text>
  <text class="caption" x="878" y="185" text-anchor="middle">Top</text>
  <text class="caption" transform="translate(1197 532) rotate(-90)" text-anchor="middle">Back</text>

  <!-- Glue flap -->
  <path class="wood" d="M68,384 V662 H32 Q16,662 16,646 V400 Q16,388 32,384 Z"/>

  <!-- Top dust flaps -->
  <path class="wood" d="M68,384 V258 Q68,243 84,243 H330 Q346,243 346,258 V384 Z"/>
  <path class="wood" d="M624,384 V258 Q624,243 640,243 H880 Q894,243 900,256 L904,262 V384 Z"/>

  <!-- Top lid with tuck -->
  <path class="wood" d="M904,384 V258 L908,252 V60 L914,50 Q920,34 940,34 H1160 Q1176,34 1180,48 L1182,60 V384 Z"/>

  <!-- Bottom flaps -->
  <path class="wood" d="M68,661 H346 L280,744 H208 V772 H232 V813 H68 Z"/>
  <path class="wood" d="M346,661 H625 V888 H538 V843 H552 V792 H418 V843 H432 V888 H346 Z"/>
  <path class="wood" d="M627,661 H904 V813 H740 V772 H764 V744 Z"/>
  <path class="wood" d="M904,661 H1184 V813 H1104 V888 H980 V813 H904 Z"/>

  <!-- Main panels -->
  <rect class="wood" x="68" y="384" width="1114" height="277"/>

  <!-- Side panel tiles -->
  <rect x="96" y="413" width="222" height="220" fill="url(#tileTone)" role="img" aria-label="Repeating tile of the brand emblem in embossed wood tones"/>
  <rect x="655" y="413" width="222" height="220" fill="url(#tileTone)" role="img" aria-label="Repeating tile of the brand emblem in embossed wood tones"/>

  <!-- Front panel -->
  <g class="front-panel">
    <rect x="421" y="384" width="131" height="277" fill="var(--ink)"/>
    <rect x="383" y="420" width="207" height="203" fill="var(--ink)"/>
    <rect class="frame-line" x="389" y="426" width="195" height="191"/>
    <rect x="421" y="384" width="131" height="32" fill="var(--ribbon)"/>
    <rect x="421" y="416" width="131" height="122" fill="var(--label-white)"/>
    <circle cx="486.5" cy="468" r="22" fill="var(--ink)"/>
    <text class="brand" x="486.5" y="528" font-size="17" text-anchor="middle">VELKA BRIN</text>
    <rect x="421" y="544" width="131" height="46" fill="var(--ribbon)"/>
    <text class="tagline" x="486.5" y="563" text-anchor="middle">100% ORGANIC PURE</text>
    <text class="tea-name" x="486.5" y="581" font-size="17" text-anchor="middle">GREEN TEA</text>
    <text class="footer-line" x="486.5" y="599" text-anchor="middle">Velka brin Herbal Tea, www.websitename.com</text>
  </g>

  <!-- Top lid ribbon -->
  <g class="lid-ribbon">
    <rect x="979" y="34" width="131" height="382" fill="var(--ribbon)"/>
    <rect x="979" y="176" width="131" height="120" fill="var(--label-white)"/>
    <circle cx="1044.5" cy="222" r="24" fill="var(--ink)"/>
    <text class="brand" x="1044.5" y="288" font-size="17" text-anchor="middle">VELKA BRIN</text>
    <text class="tagline" x="1044.5" y="323" text-anchor="middle">100% ORGANIC PURE</text>
    <text class="tea-name" x="1044.5" y="340" font-size="17" text-anchor="middle">GREEN TEA</text>
  </g>

  <!-- Back panel -->
  <g class="back-panel">
    <rect x="979" y="416" width="131" height="245" fill="var(--ink)"/>
    <rect x="942" y="420" width="206" height="203" fill="var(--ink)"/>
    <rect class="frame-line" x="948" y="426" width="194" height="191"/>
    <rect x="964" y="438" width="164" height="156" fill="var(--note)"/>
    <g fill="var(--ink)">
      <circle cx="969" cy="450" r="1.6"/><circle cx="969" cy="462" r="1.6"/><circle cx="969" cy="474" r="1.6"/>
      <circle cx="969" cy="486" r="1.6"/><circle cx="969" cy="498" r="1.6"/><circle cx="969" cy="510" r="1.6"/>
      <circle cx="969" cy="522" r="1.6"/><circle cx="969" cy="534" r="1.6"/><circle cx="969" cy="546" r="1.6"/>
      <circle cx="969" cy="558" r="1.6"/><circle cx="969" cy="570" r="1.6"/><circle cx="969" cy="582" r="1.6"/>
    </g>
    <text class="note-head" x="993" y="459">About The Tea</text>
    <text class="note-body" x="993" y="467">Lorem ipsum dolor sit amet, consectetur</text>
    <text class="note-body" x="993" y="474">adipiscing elit. Duis euismod odio quis</text>
    <text class="note-body" x="993" y="481">ligula consequat, non iaculis augue sce</text>
    <text class="note-body" x="993" y="488">lerisque. Nam non turpis eu massa fa u</text>
    <text class="note-body" x="993" y="495">cibus euismod vitae nec ante.</text>
    <text class="note-head" x="993" y="517">How we like it</text>
    <text class="note-body" x="993" y="525">Lorem ipsum dolor sit amet, consectetur</text>
    <text class="note-body" x="993" y="532">adipiscing elit. Duis euismod odio quis</text>
    <text class="note-body" x="993" y="539">ligula consequat, non iaculis.</text>
    <g fill="none" stroke="var(--ink)" stroke-width="0.9">
      <rect x="998" y="548" width="10" height="10" transform="rotate(-15 1003 553)"/>
      <path d="M1046,558 h14 l-2,-8 a5,5 0 0 0 -10,0 z"/>
      <circle cx="1097" cy="553" r="6"/>
      <path d="M1097,549 v4 h3"/>
      <path d="M1029,562 v12 M1076,562 v12" stroke-dasharray="1.5 1.5"/>
    </g>
    <text class="note-body" x="1004" y="571" text-anchor="middle">1 tea bag</text>
    <text class="note-body" x="1004" y="577" text-anchor="middle">per person</text>
    <text class="note-body" x="1053" y="571" text-anchor="middle">Water</text>
    <text class="note-body" x="1053" y="577" text-anchor="middle">80°C</text>
    <text class="note-body" x="1098" y="571" text-anchor="middle">Brew</text>
    <text class="note-body" x="1098" y="577" text-anchor="middle">3-5 mins</text>
    <text class="note-body" x="991" y="590">Net Wt. 80 G    MFD | Lot | Exp :</text>
    <text class="footer-line" x="1045" y="603" text-anchor="middle">Velka brin Herbal Tea, www.websitename.com</text>
  </g>

  <!-- Fold lines around the four panels -->
  <rect class="panel-edge" x="69.5" y="385.5" width="277" height="275"/>
  <rect class="panel-edge" x="350.5" y="385.5" width="275" height="275"/>
  <rect class="panel-edge" x="628.5" y="385.5" width="276" height="275"/>
  <rect class="panel-edge" x="907.5" y="385.5" width="274" height="275"/>
</svg>
</div>
</body>
</html>
```